Stress Fracture Infographic for Scientific Paper

We need an infographic for a research/scientific paper. We would like the infographic to give readers a clear and eye-catching overview about the factors that put athletes and military personnel at risk for stress fractures. The design needs to communicate that the risk factors are cumulative and interactive; however, how they specifically accumulate and interact has not been studied or shown in the literature (we need healthcare providers who subjectively assess cumulative risk profiles in athletes and we concurrently need scientists to evaluate the interdependence of risk factors). We define cumulative risk profile as: a subjective clinical determination of the number of factors putting an athlete at risk along with thoughtful consideration regarding how all the risk factors interact with one another. We would like the infographic to display this cumulative risk profile idea.

The risk factors can be categorized as:
INTRINSIC-
Non-modifiable (such as sex, race, age, genetics, anatomical structure, and prior bone stress injury), modifiable (muscle strength, muscle fatigue, flexibility, biomechanics, stress, recovery strategies, nutrition, energy deficiency), unclear if modifiable, not, or somewhere in between (such as gut health);

EXTRINSIC-
Modifiable (footwear, training surface, workload)

Target Market(s)

Researchers and clinicians

Requirements
Must have
• A scientific feel
Nice to have
• Creative way to display the cumulative and interactive impact of risk factors
Should not have
• Too cartoon-ish or child-like feel

```html
<!DOCTYPE html>
<html lang="en">
<head>
<meta charset="utf-8">
<title>The Risk Factors</title>
<link href="https://fonts.googleapis.com/css2?family=Oswald:wght@500;700&family=Open+Sans:wght@400;600;700&display=swap" rel="stylesheet">
<style>
:root{
  --teal:#0f8c9c;
  --teal-dark:#0a5f6d;
  --teal-light:#4fb3bf;
  --tint:#e6f2f4;
  --ink:#1d3a42;
  --white:#ffffff;
  --line:#0a5f6d;
}
*{box-sizing:border-box;margin:0;padding:0}
html,body{width:863px;height:1200px;overflow:hidden;background:var(--white)}
body{font-family:"Open Sans",Arial,sans-serif;color:var(--ink);position:relative}
.poster{position:absolute;inset:0;background:linear-gradient(180deg,#f7fbfc 0%,#ffffff 40%,#ffffff 100%)}
.title-ribbon{position:absolute;left:160px;top:20px;width:543px;height:64px}
.title-ribbon svg{position:absolute;inset:0}
.title{position:absolute;inset:0;display:flex;align-items:center;justify-content:center;font-family:"Oswald",Arial,sans-serif;font-weight:700;font-size:38px;letter-spacing:1px;color:var(--white)}
.lede{position:absolute;left:110px;top:92px;width:643px;text-align:center;font-size:14px;line-height:1.35;font-weight:600;color:var(--ink)}
.pill{position:absolute;top:160px;height:50px;border-radius:25px;border:3px solid var(--teal);background:var(--white);display:flex;align-items:center;justify-content:center}
.pill span{display:block;margin:0 6px;width:calc(100% - 12px);height:36px;border-radius:18px;background:var(--teal);color:var(--white);font-family:"Oswald",Arial,sans-serif;font-weight:700;font-size:24px;letter-spacing:1px;text-align:center;line-height:36px}
.pill-intrinsic{left:140px;width:210px}
.pill-extrinsic{left:562px;width:206px}
.connectors{position:absolute;inset:0;pointer-events:none}
.column{position:absolute;top:288px;display:flex;flex-direction:column;align-items:stretch}
.col-head{height:86px;background:var(--white);border:3px solid var(--teal-dark);border-radius:0 0 16px 16px;display:flex;align-items:center;justify-content:center;text-align:center;font-family:"Oswald",Arial,sans-serif;font-weight:500;font-size:14px;line-height:1.15;color:var(--teal-dark);padding:4px}
.col-body{margin-top:8px;background:var(--teal);border-radius:4px;padding:10px 6px 14px;display:flex;flex-direction:column;align-items:center}
.col-nonmod .col-body{background:var(--teal-light)}
.such-as{font-family:"Oswald",Arial,sans-serif;font-size:13px;letter-spacing:1px;color:var(--white);border-top:1px solid rgba(255,255,255,.7);border-bottom:1px solid rgba(255,255,255,.7);padding:1px 8px;margin-bottom:12px}
.factor{display:flex;flex-direction:column;align-items:center;text-align:center;color:var(--white);font-size:13px;font-weight:600;line-height:1.2;height:92px}
.factor svg{width:38px;height:38px;margin-bottom:6px}
.col-nonmod{left:30px;width:104px}
.col-mod{left:150px;width:172px}
.col-between{left:342px;width:134px}
.col-ext{left:590px;width:150px}
.illustration{position:absolute;left:478px;top:770px;width:365px;height:410px;border-radius:22px;background:radial-gradient(circle at 60% 55%,#cfe9ee 0%,#e8f4f6 55%,rgba(255,255,255,0) 75%)}
</style>
</head>
<body>
<main class="poster">
  <header class="title-ribbon">
    <svg viewBox="0 0 543 64" aria-hidden="true">
      <polygon points="0,14 40,14 40,58 0,58 14,36" fill="var(--teal-dark)"/>
      <polygon points="543,14 503,14 503,58 543,58 529,36" fill="var(--teal-dark)"/>
      <rect x="28" y="4" width="487" height="50" fill="var(--teal)"/>
    </svg>
    <h1 class="title">THE RISK FACTORS</h1>
  </header>
  <p class="lede">A subjective clinical determination of the number of factors putting an athlete at risk along with thoughtful consideration regarding how all the risk factors interact with one another.</p>

  <svg class="connectors" viewBox="0 0 863 1200" aria-hidden="true">
    <g stroke="var(--line)" stroke-width="3" fill="none">
      <line x1="245" y1="210" x2="245" y2="252"/>
      <line x1="82" y1="252" x2="409" y2="252"/>
      <line x1="82" y1="252" x2="82" y2="288"/>
      <line x1="236" y1="252" x2="236" y2="288"/>
      <line x1="409" y1="252" x2="409" y2="288"/>
      <line x1="665" y1="210" x2="665" y2="288"/>
    </g>
  </svg>

  <div class="pill pill-intrinsic"><span>INTRINSIC</span></div>
  <div class="pill pill-extrinsic"><span>EXTRINSIC</span></div>

  <section class="column col-nonmod">
    <div class="col-head">NON-<br>MODIFIABLE</div>
    <div class="col-body">
      <div class="such-as">SUCH AS</div>
      <div class="factor"><svg viewBox="0 0 40 40" fill="none" stroke="#fff" stroke-width="2.5"><circle cx="17" cy="22" r="8"/><path d="M23 16l9-9M26 7h6v6"/></svg>Sex</div>
      <div class="factor"><svg viewBox="0 0 40 40" fill="none" stroke="#fff" stroke-width="2.5"><circle cx="20" cy="20" r="14"/><path d="M6 20h28M20 6c-6 8-6 20 0 28M20 6c6 8 6 20 0 28"/></svg>Race</div>
      <div class="factor"><svg viewBox="0 0 40 40" fill="none" stroke="#fff" stroke-width="2.5"><path d="M11 5h18M11 35h18M13 5c0 10 14 10 14 15s-14 5-14 15M27 5c0 10-14 10-14 15s14 5 14 15"/></svg>Age</div>
      <div class="factor"><svg viewBox="0 0 40 40" fill="none" stroke="#fff" stroke-width="2.5"><path d="M13 4c0 12 14 20 14 32M27 4c0 12-14 20-14 32M15 11h10M15 29h10M18 20h4"/></svg>Genetics</div>
      <div class="factor"><svg viewBox="0 0 40 40" fill="none" stroke="#fff" stroke-width="2.5"><circle cx="20" cy="7" r="4"/><path d="M20 11v14M10 16h20M20 25l-6 11M20 25l6 11"/></svg>Anatomical structure</div>
      <div class="factor"><svg viewBox="0 0 40 40" fill="none" stroke="#fff" stroke-width="2.5"><path d="M8 32l24-24M6 28a4 4 0 1 1 6 6M34 12a4 4 0 1 1-6-6M18 18l4 4"/></svg>Prior bone stress injury</div>
    </div>
  </section>

  <section class="column col-mod">
    <div class="col-head">MODIFIABLE</div>
    <div class="col-body">
      <div class="such-as">SUCH AS</div>
      <div class="factor"><svg viewBox="0 0 40 40" fill="none" stroke="#fff" stroke-width="2.5"><path d="M4 20h32M8 13v14M12 10v20M28 10v20M32 13v14"/></svg>Muscle Strength</div>
      <div class="factor"><svg viewBox="0 0 40 40" fill="none" stroke="#fff" stroke-width="2.5"><rect x="5" y="13" width="26" height="14" rx="2"/><path d="M34 18v4M9 17v6"/></svg>Muscle Fatigue</div>
      <div class="factor"><svg viewBox="0 0 40 40" fill="none" stroke="#fff" stroke-width="2.5"><circle cx="26" cy="7" r="4"/><path d="M24 12l-6 10 10 4M18 22l-10 8M28 26l6 8"/></svg>Flexibility</div>
      <div class="factor"><svg viewBox="0 0 40 40" fill="none" stroke="#fff" stroke-width="2.5"><circle cx="22" cy="6" r="4"/><path d="M21 11l-3 12 7 5v8M18 23l-8 11M20 14l8 5M20 14l-8 3"/></svg>Biomechanics</div>
      <div class="factor"><svg viewBox="0 0 40 40" fill="none" stroke="#fff" stroke-width="2.5"><circle cx="20" cy="20" r="14"/><path d="M13 15l4 2M27 15l-4 2M13 28c3-3 11-3 14 0"/></svg>Stress</div>
      <div class="factor"><svg viewBox="0 0 40 40" fill="none" stroke="#fff" stroke-width="2.5"><path d="M33 20a13 13 0 1 1-4-9.5M33 6v8h-8"/></svg>Recovery strategies</div>
      <div class="factor"><svg viewBox="0 0 40 40" fill="none" stroke="#fff" stroke-width="2.5"><path d="M20 12c-8-5-14 2-12 10s7 13 12 11c5 2 10-3 12-11s-4-15-12-10zM20 12c0-4 2-7 5-8"/></svg>Nutrition</div>
      <div class="factor"><svg viewBox="0 0 40 40" fill="none" stroke="#fff" stroke-width="2.5"><rect x="5" y="12" width="26" height="16" rx="2"/><path d="M34 17v6"/><path d="M18 14l-4 7h6l-4 6"/></svg>Energy deficiency</div>
    </div>
  </section>

  <section class="column col-between">
    <div class="col-head">SOMEWHERE<br>IN<br>BETWEEN</div>
    <div class="col-body">
      <div class="such-as">SUCH AS</div>
      <div class="factor"><svg viewBox="0 0 40 40" fill="none" stroke="#fff" stroke-width="2.5"><path d="M14 5v8c0 4-8 5-8 13s7 10 12 8 4-7 10-7 7-6 6-11-6-5-8-3-4 2-4-2V5"/></svg>Gut Health</div>
    </div>
  </section>

  <section class="column col-ext">
    <div class="col-head">MODIFIABLE</div>
    <div class="col-body">
      <div class="such-as">SUCH AS</div>
      <div class="factor"><svg viewBox="0 0 40 40" fill="none" stroke="#fff" stroke-width="2.5"><path d="M6 14l8 2 6 6 12 3c3 1 3 7 0 7H6z"/><path d="M6 27h28"/></svg>Footwear</div>
      <div class="factor"><svg viewBox="0 0 40 40" fill="none" stroke="#fff" stroke-width="2.5"><rect x="5" y="8" width="30" height="24" rx="12"/><rect x="12" y="14" width="16" height="12" rx="6"/></svg>Training Surface</div>
      <div class="factor"><svg viewBox="0 0 40 40" fill="none" stroke="#fff" stroke-width="2.5"><path d="M10 14h20l4 20H6zM15 14a5 5 0 1 1 10 0"/></svg>Workload</div>
    </div>
  </section>

  <div class="illustration" role="img" aria-label="Illustration of a clinician reviewing floating medical profile cards with a health cross symbol"></div>
</main>
</body>
</html>
```